GUARANTEED 4 sample word cards for inclusive primary education (the swan, the icebear, the cat, sad)

in short: it's about drawing a swan, at icebear, a cat, a sad person (male / female) and arranging them on word cards with some additional information As there which only one design submitted, Which was missing the point I Decided to translate everything myself and upload it again. Requirements Within an open educational ressources (OER) project, materials for the interest-based spelling workout are to be created. In the preparation of this project four example sample word cards are to be developed. Later They Should be compiled dynamically from a database. Since the needs of the teachers are very different, it would be advantageous to integrate the different design elements as layers in Photoshop so did one can show how diverse the cards can look later by hiding / showing the layers. The materials shoulderstand be distributed under cc-0 license. It is about 4 sample cards (the swan, the icebear, the cat, sad), Which shoulderstand demonstrate how search cards can look. German: As part of an OER project are materials to interest-based spelling learning occur. In the preparation of the project (to be created also a permanent position for a / n Designer / -in under which) are four examplarische Sample word cards are developed. Later this should be assembled dynamically from a database. Since the needs of teachers / -Innen are very different, it would be desirable to integrate the various design elements as layers in Photoshop, so you can show how diverse can look the cards later. The materials are to be distributed under cc-0 license. It is about 4 example cards that demonstrate how can such cards look. The most expensive part is undoubtedly the drawings (polar bear, swan, cat and sad child / sad person). Common elements - speech symbol Veldarini (see http: //media.lirobeck-press. example / media / catalog / product / cache / 4 / image / 3ab51cde90417f62c8e0a4d19253b78a / 0/7 / 04189_1.jpg) - underline articles colored or colored or point mark (male - red, male - blue, neuter - green) - writing of definition and article (once https://glyphshelf.example/en/font/grundschrift and once a school Ausgangsschrift eg https://www.tomvaro.example/hub/Lumen/de_DE.CMS.displayCMS.318406./die-schulausgangsschrift -sas-free-download-tomvaro) - Ruling based on http://www.b-straleck.example/wp-content/uploads/2010/01/Heft-006-innen.png (and even without house) - picture on the right side - pictures with people, each as a girl / boy, different skin colors (or all as layers in Photoshop, where I can hide it myself) - syllable sheets (instead of the | http://trymindquill.example/wp- content / uploads / 2015_2_Silbenboegen_Kombo.png) - colored syllables (blue and red) - stem color (red), ending black - cases if necessary on the back of the card - Format Din A7, rounded corners images should as svg / or levels exist (different skin color / hair color / gender) drawings should stylized and not be too childish and love of detail, so that they are attractive to adults (and as can be used in work with fugitives). You should also black / white and be usable with red / green blindness. The exact requirements are in the description file. For any questions please contact via the platform or haraldp.ostwig@hs-varnholt.example Ps: If a logo for (spelling) learning, including drops, it is also nich bad;) If you interested in a long-term employment in a project have the university, we appreciate if you mention this.
pupils in primary school, so but older students and adults (for example refugees who started to learn the language) students / -Innen primary school (until fourth grade) as well as older adolescents / adults, therefore, not to child pictures
Education
- see additional file

- psd files with levels, to show and hide different elements self drawn images, Which Could be released under a CC-0 license. see additional file for more info and sample German: .psd files with labeled layers, in which the individual elements can be hidden. Self-drawn graphics which can then be released under cc-0 Stock

```html
<!DOCTYPE html>
<html lang="de">
<head>
<meta charset="utf-8">
<title>Wortkarte – die Katze</title>
<link rel="stylesheet" href="https://fonts.googleapis.com/css2?family=Andika:wght@400;700&display=swap">
<style>
  :root {
    --frame: #c6dff1;
    --accent: #1ea7e1;
    --ink: #1a1a1a;
    --muted: #555555;
    --row: #c6dff1;
    --paper: #ffffff;
    --shadow: rgba(40, 40, 40, 0.75);
  }
  * { margin: 0; padding: 0; box-sizing: border-box; }
  html, body { width: 927px; height: 1200px; overflow: hidden; background: var(--paper); }
  body { position: relative; font-family: "Andika", "Comic Sans MS", sans-serif; color: var(--ink); }

  .card {
    position: absolute; left: 161px; width: 635px;
    background: var(--frame);
    box-shadow: 6px 7px 6px var(--shadow);
  }
  .card--front { top: 98px; height: 453px; }
  .card--back { top: 611px; height: 449px; }
  .card__inner {
    position: absolute; left: 11px; top: 12px; right: 13px; bottom: 15px;
    background: var(--paper); border-radius: 17px;
  }

  .abs { position: absolute; }

  .noun-icon { left: 210px; top: 147px; }
  .word { font-size: 40px; line-height: 1; white-space: nowrap; }
  .word--singular { left: 265px; top: 196px; }
  .word--plural { left: 259px; top: 270px; }
  .article { color: var(--accent); }
  .example { left: 210px; top: 350px; font-size: 17px; color: var(--muted); }
  .tags { left: 210px; top: 406px; font-size: 17px; color: var(--muted); }
  .article-symbol { left: 382px; top: 447px; }
  .article-label { left: 465px; top: 458px; font-size: 34px; color: var(--accent); line-height: 1; }

  .picture-frame {
    left: 489px; top: 145px; width: 283px; height: 235px;
    border: 1.5px solid var(--ink); border-radius: 20px; overflow: hidden;
  }
  .picture {
    position: absolute; left: 70px; top: 6px; width: 140px; height: 220px;
    background: linear-gradient(180deg, #f2f2f2, #dcdcdc);
    border-radius: 40px 40px 20px 20px;
  }

  .case-table { left: 189px; top: 715px; width: 579px; height: 214px; font-size: 18px; }
  .case-table__head {
    position: absolute; top: 0; height: 45px; line-height: 50px; z-index: 1; white-space: nowrap;
  }
  .case-table__head--sg { left: 277px; }
  .case-table__head--pl { left: 481px; }
  .case-row {
    position: absolute; left: 0; width: 579px; height: 41px; line-height: 41px; white-space: nowrap;
  }
  .case-row--shaded { background: var(--row); }
  .case-row--nom { top: 45px; border-radius: 12px 0 0 0; }
  .case-row--gen { top: 86px; }
  .case-row--dat { top: 127px; }
  .case-row--akk { top: 168px; }
  .case-row__label { position: absolute; left: 9px; }
  .case-row__sg { position: absolute; left: 266px; color: var(--muted); }
  .case-row__pl { position: absolute; left: 458px; color: var(--muted); }
  .case-table__outline { position: absolute; left: 0; top: 0; z-index: 2; }
</style>
</head>
<body>

<section class="card card--front">
  <div class="card__inner"></div>
</section>

<svg class="abs noun-icon" width="48" height="96" viewBox="0 0 48 96" aria-hidden="true">
  <polygon points="24,0 47,31 1,31" fill="var(--accent)"/>
  <rect x="10.5" y="31" width="27" height="21" fill="none" stroke="var(--ink)" stroke-width="1.5"/>
  <rect x="10.5" y="52" width="27" height="21" fill="none" stroke="var(--ink)" stroke-width="1.5"/>
  <rect x="10.5" y="73" width="27" height="21" fill="none" stroke="var(--ink)" stroke-width="1.5"/>
</svg>
<p class="abs word word--singular"><span class="article">die</span> Katze</p>
<p class="abs word word--plural">die Katzen</p>
<p class="abs example">Die Katze schläft.</p>
<p class="abs tags">Tier | Haustier | Säugetier | mittelgroß ;)</p>

<svg class="abs article-symbol" width="72" height="68" viewBox="0 0 72 68" aria-hidden="true">
  <polygon points="36,0 72,68 0,68" fill="var(--accent)"/>
</svg>
<p class="abs article-label">Artikel</p>

<div class="abs picture-frame">
  <div class="picture" role="img" aria-label="Zeichnung einer sitzenden getigerten Katze"></div>
</div>

<section class="card card--back">
  <div class="card__inner"></div>
</section>

<div class="abs case-table">
  <span class="case-table__head case-table__head--sg">Singular</span>
  <span class="case-table__head case-table__head--pl">Plural</span>
  <div class="case-row case-row--nom case-row--shaded">
    <span class="case-row__label">Nominativ (wer?/was?)</span>
    <span class="case-row__sg">die Katze</span>
    <span class="case-row__pl">die Katzen</span>
  </div>
  <div class="case-row case-row--gen">
    <span class="case-row__label">Genitiv (wessen?)</span>
    <span class="case-row__sg">der Katze</span>
    <span class="case-row__pl">der Katzen</span>
  </div>
  <div class="case-row case-row--dat case-row--shaded">
    <span class="case-row__label">Dativ (wem?)</span>
    <span class="case-row__sg">der Katze</span>
    <span class="case-row__pl">den Katzen</span>
  </div>
  <div class="case-row case-row--akk">
    <span class="case-row__label">Akkusativ (wen?/was?)</span>
    <span class="case-row__sg">die Katze</span>
    <span class="case-row__pl">die Katzen</span>
  </div>
  <svg class="case-table__outline" width="579" height="214" viewBox="0 0 579 214" aria-hidden="true">
    <path d="M249.75,45 V12.75 A12,12 0 0 1 261.75,0.75 H566.25 A12,12 0 0 1 578.25,12.75 V201.25 A12,12 0 0 1 566.25,213.25 H12.75 A12,12 0 0 1 0.75,201.25 V57 A12,12 0 0 1 12.75,45 H249.75"
          fill="none" stroke="var(--ink)" stroke-width="1.5"/>
  </svg>
</div>

</body>
</html>
```